Realty Group Needs Classy, Contemporary Letterhead Design

We need a letterhead design for a new realty company located in NY, USA. We buy investment properties to rehabilitate and or keep in our rental portfolio.

```html
<!DOCTYPE html>
<html lang="en">
<head>
<meta charset="UTF-8">
<title>Meridian Realty Group – Letterhead</title>
<link href="https://fonts.googleapis.com/css2?family=Poppins:wght@400;500;600;800&family=Great+Vibes&family=Oswald:wght@400&display=swap" rel="stylesheet">
<style>
  :root {
    --brand-purple: #4e2a84;
    --ink-grey: #5a5a5a;
    --rule-grey: #6b6b6b;
    --roof-grey: #ececf0;
    --paper: #ffffff;
    --artboard: #cccccc;
  }
  * { margin: 0; padding: 0; box-sizing: border-box; }
  html, body { width: 927px; height: 1200px; overflow: hidden; background: var(--artboard); }
  .canvas { position: relative; width: 927px; height: 1200px; }
  .page {
    position: absolute; left: 64px; top: 41px; width: 798px; height: 1121px;
    background: var(--paper); overflow: hidden;
  }
  .page-art { position: absolute; left: 0; top: 0; }
  .brand-name {
    position: absolute; left: 144px; top: 80px;
    font: 800 54px/1 "Poppins", sans-serif; color: var(--brand-purple); letter-spacing: -1px;
  }
  .brand-tagline {
    position: absolute; left: 144px; top: 137px; width: 330px;
    display: flex; align-items: center; gap: 10px;
    font: 500 16px/1 "Poppins", sans-serif; color: var(--ink-grey); letter-spacing: 1px;
  }
  .brand-tagline::before, .brand-tagline::after { content: ""; flex: 1; height: 1.5px; background: var(--ink-grey); }
  .sender-role {
    position: absolute; left: 150px; top: 169px;
    font: 600 12px/1 "Poppins", sans-serif; color: var(--ink-grey); letter-spacing: 2px;
  }
  .sender-address {
    position: absolute; left: 150px; top: 196px;
    font: 400 13px/18px "Poppins", sans-serif; color: var(--ink-grey); letter-spacing: 2px;
  }
  .signature {
    position: absolute; left: 116px; top: 800px;
    font: 400 52px/1 "Great Vibes", cursive; color: #333; transform: rotate(-6deg);
  }
  .signer-name {
    position: absolute; left: 210px; top: 849px;
    font: 400 27px/1 "Oswald", sans-serif; color: var(--brand-purple); transform: scaleX(0.85); transform-origin: left;
  }
  .contact-item {
    position: absolute; left: 116px;
    font: 400 12px/18px "Poppins", sans-serif; color: #333; letter-spacing: 1.6px;
  }
</style>
</head>
<body>
<div class="canvas">
  <div class="page">
    <svg class="page-art" width="798" height="1121" viewBox="0 0 798 1121" aria-hidden="true">
      <!-- side bands -->
      <rect x="0" y="0" width="41" height="1121" fill="var(--brand-purple)"/>
      <rect x="68" y="0" width="7" height="1121" fill="var(--brand-purple)"/>
      <!-- header pointer -->
      <polygon points="75,88 115,108 75,129" fill="var(--brand-purple)"/>
      <!-- roof stripes -->
      <polygon points="584,206 676,42 698,42 606,206" fill="var(--roof-grey)"/>
      <polygon points="624,206 716,42 738,42 646,206" fill="var(--roof-grey)"/>
      <polygon points="756,42 798,42 798,110" fill="var(--roof-grey)"/>
      <!-- body rules -->
      <g stroke="var(--rule-grey)" stroke-width="1.2">
        <line x1="197" y1="365" x2="689" y2="365"/>
        <line x1="157" y1="386" x2="689" y2="386"/>
        <line x1="157" y1="407" x2="689" y2="407"/>
        <line x1="157" y1="427" x2="689" y2="427"/>
        <line x1="157" y1="448" x2="689" y2="448"/>
        <line x1="157" y1="470" x2="689" y2="470"/>
        <line x1="157" y1="491" x2="337" y2="491"/>
        <line x1="157" y1="527" x2="689" y2="527"/>
        <line x1="157" y1="548" x2="689" y2="548"/>
        <line x1="157" y1="570" x2="689" y2="570"/>
        <line x1="157" y1="589" x2="689" y2="589"/>
        <line x1="157" y1="610" x2="689" y2="610"/>
        <line x1="157" y1="632" x2="689" y2="632"/>
        <line x1="157" y1="651" x2="689" y2="651"/>
        <line x1="157" y1="673" x2="447" y2="673"/>
        <line x1="157" y1="713" x2="689" y2="713"/>
        <line x1="157" y1="735" x2="613" y2="735"/>
      </g>
      <!-- corner triangle -->
      <polygon points="798,727 580,841 798,962" fill="var(--brand-purple)"/>
      <!-- contact icons -->
      <g class="contact-icons">
        <rect x="61" y="975" width="20" height="20" transform="rotate(45 71 985)" fill="var(--paper)" stroke="var(--brand-purple)" stroke-width="2"/>
        <rect x="65" y="981" width="12" height="8" fill="var(--brand-purple)"/>
        <polyline points="65,981 71,986 77,981" fill="none" stroke="var(--paper)" stroke-width="1"/>
        <rect x="61" y="1013" width="20" height="20" transform="rotate(45 71 1023)" fill="var(--brand-purple)"/>
        <path d="M67 1017 q-1 6 4 10 q4 3 6 1 l-2 -3 l-2 1 q-3 -2 -4 -5 l1 -2 z" fill="var(--paper)"/>
        <rect x="61" y="1050" width="20" height="20" transform="rotate(45 71 1060)" fill="var(--paper)" stroke="var(--brand-purple)" stroke-width="2"/>
        <circle cx="71" cy="1060" r="6" fill="var(--brand-purple)"/>
        <circle cx="71" cy="1059" r="2" fill="var(--paper)"/>
      </g>
    </svg>

    <div class="brand-name">MERIDIAN</div>
    <div class="brand-tagline">Realty Group, LLC</div>
    <div class="sender-role">Managing Director.</div>
    <div class="sender-address">Street name, City Name,<br>State, Country, 12345</div>

    <div class="signature">Signature</div>
    <div class="signer-name">Your Name</div>

    <div class="contact-item" style="top:976px;">hello@meridianrealty.com</div>
    <div class="contact-item" style="top:1014px;">+00 987 654 3210</div>
    <div class="contact-item" style="top:1047px;">Street name, City Name,<br>State, Country, 12345</div>
  </div>
</div>
</body>
</html>
```